Service Menu refresh 2018 Update of menu pricing

We currently have service menus as attached. We will be updating our look via our homepage image, our service menu and our in-house beverage and treatment menu.
We are a natural and sustainable hair salon group and moving more towards head spa which consists of treatments, beauty, tanning as well as your traditional hair services. Our imagery needs to reflect our efforts in spa treatments in the hair and scalp area and use natural materials and colours reflecting sustainability.
Velin is the brand we stock and promote.

Target Market(s)

Men or women interesting in personal maintenance with natural and organic products and using sustainable practises

Industry/Entity Type

Hair And Beauty

Font styles to use
Sans Serif
Other font styles liked:
• Arial or Helvetica

Colors
9acb3c
abd037
cadf82
ffffff

Requirements
Must have
• Name on the front cover, locations on back cover
Nice to have
• Prestige feel, reflect male and female clients
Should not have
• Bold artificial writing or any type of cartoon images.
• Same images as existing menu.

```html
<!DOCTYPE html>
<html lang="en">
<head>
<meta charset="utf-8">
<title>Purely Rooted Hair Salons – Service Menu</title>
<link href="https://fonts.googleapis.com/css2?family=Source+Sans+3:wght@300;400;600&display=swap" rel="stylesheet">
<style>
:root{
  --stage:#e9e7e3;
  --paper:#f2f2f1;
  --ink:#2a2a2a;
  --ink-soft:#555;
  --green:#8cc63f;
  --green-deep:#3f6a36;
  --menu-green:#7ab648;
  --white:#ffffff;
}
*{margin:0;padding:0;box-sizing:border-box}
html,body{width:1200px;height:1151px;overflow:hidden;background:var(--stage);font-family:"Source Sans 3",Arial,sans-serif}
.card{position:absolute;left:98px;width:1115px;height:605px;transform:scale(.9);transform-origin:0 0;overflow:hidden;box-shadow:0 3px 10px rgba(0,0,0,.25)}
.card-front{top:15px;background:var(--paper);color:var(--ink)}
.card-back{top:590px;background:var(--menu-green);color:var(--white)}
.front-art{position:absolute;left:0;top:0}
.brand{position:absolute;display:flex;align-items:center;gap:14px;font-weight:400;white-space:nowrap}
.brand-dot{border-radius:50%;flex:none}
.card-front .brand{left:560px;top:36px;font-size:40px;color:var(--ink);letter-spacing:-.5px}
.card-front .brand-dot{width:58px;height:58px;background:var(--green)}
.location{position:absolute;left:658px;font-size:16px;color:var(--ink-soft);line-height:21px}
.location h3{font-weight:400;font-size:20px;color:var(--ink);line-height:24px;display:flex;align-items:center;gap:10px}
.location h3 svg{flex:none}
.location b{font-weight:400;color:var(--ink)}
.location .mail{margin-left:12px}
.web{position:absolute;left:715px;top:548px;width:400px;height:44px;border-radius:22px 0 0 22px;background:var(--green);color:var(--white);font-size:19px;letter-spacing:.5px;line-height:44px;padding-left:23px}
.leaf-art{position:absolute;right:0;top:0;width:440px;height:605px;background:radial-gradient(ellipse at 70% 30%,rgba(255,255,255,.12),transparent 60%),linear-gradient(120deg,rgba(122,182,72,0) 0%,rgba(80,140,50,.35) 55%,rgba(60,120,40,.45) 100%)}
.card-back .brand{left:40px;top:40px;font-size:42px;color:var(--white);letter-spacing:-.5px}
.card-back .brand-dot{width:64px;height:64px;background:var(--white)}
.note{position:absolute;left:583px;top:34px;width:480px;height:77px;border:1.5px solid var(--white);font-size:12.5px;line-height:15.5px;padding:12px 12px}
.menu{position:absolute;top:0;width:475px;height:605px}
.menu-left{left:33px}
.menu-right{left:583px}
.head{position:absolute;left:0;width:100%;height:24px;font-size:20px;line-height:24px;font-weight:400}
.rule{position:absolute;left:0;width:473px;height:1.5px;background:var(--white)}
.row{position:absolute;left:0;width:100%;height:16px;line-height:16px;font-size:12.5px}
.row.cap{font-size:15px;letter-spacing:.2px}
.c1,.c2,.c3,.c4,.h1,.h2,.h3,.h4{position:absolute;top:0;font-size:12.5px}
.head .h1,.head .h2,.head .h3,.head .h4{font-size:20px}
.c1{left:310px}.c2{left:350px}.c3{left:399px}.c4{left:440px}
.h1{left:315px}.h2{left:359px}.h3{left:404px}.h4{left:448px}
</style>
</head>
<body>

<section class="card card-front">
  <svg class="front-art" width="1115" height="605" viewBox="0 0 1115 605">
    <defs>
      <linearGradient id="salonTones" x1="0" y1="0" x2="1" y2="1">
        <stop offset="0" stop-color="#cfd3cd"/>
        <stop offset=".45" stop-color="#b7bcb3"/>
        <stop offset="1" stop-color="#8f958a"/>
      </linearGradient>
    </defs>
    <path d="M0 0H500C570 150 582 400 540 605H0Z" fill="var(--green-deep)"/>
    <path d="M0 0H490C555 150 565 390 505 605H0Z" fill="var(--green)"/>
    <path d="M0 0H478C545 140 560 380 447 605H0Z" fill="url(#salonTones)" role="img" aria-label="Sketch of the salon interior with shelving, styling chairs and hanging plants"/>
  </svg>

  <div class="brand"><span class="brand-dot"></span>Purely Rooted Hair Salons</div>

  <div class="location" style="top:128px">
    <h3><svg width="12" height="16" viewBox="0 0 12 16"><path d="M6 0a6 6 0 0 0-6 6c0 4.5 6 10 6 10s6-5.5 6-10a6 6 0 0 0-6-6zm0 8.5A2.5 2.5 0 1 1 6 3.5a2.5 2.5 0 0 1 0 5z" fill="#8cc63f"/></svg>ELMWOOD</h3>
    <p>Brook Road, Elmwood Central, 4152</p>
    <p><b>p:</b> 07 5550 1184<span class="mail"><b>e:</b> elmwood@purelyrooted.com.au</span></p>
  </div>
  <div class="location" style="top:212px">
    <h3><svg width="12" height="16" viewBox="0 0 12 16"><path d="M6 0a6 6 0 0 0-6 6c0 4.5 6 10 6 10s6-5.5 6-10a6 6 0 0 0-6-6zm0 8.5A2.5 2.5 0 1 1 6 3.5a2.5 2.5 0 0 1 0 5z" fill="#8cc63f"/></svg>ASHGROVE PARK</h3>
    <p>Harlow Road, Ashgrove Park Plaza, 4032</p>
    <p><b>p:</b> 07 5550 2267<span class="mail"><b>e:</b> ashgrove@purelyrooted.com.au</span></p>
  </div>
  <div class="location" style="top:296px">
    <h3><svg width="12" height="16" viewBox="0 0 12 16"><path d="M6 0a6 6 0 0 0-6 6c0 4.5 6 10 6 10s6-5.5 6-10a6 6 0 0 0-6-6zm0 8.5A2.5 2.5 0 1 1 6 3.5a2.5 2.5 0 0 1 0 5z" fill="#8cc63f"/></svg>KESTREL BAY</h3>
    <p>Marden Road, Kestrel Bay Shopping Centre, 4068</p>
    <p><b>p:</b> 07 5550 3391<span class="mail"><b>e:</b> kestrelbay@purelyrooted.com.au</span></p>
  </div>
  <div class="location" style="top:381px">
    <h3><svg width="12" height="16" viewBox="0 0 12 16"><path d="M6 0a6 6 0 0 0-6 6c0 4.5 6 10 6 10s6-5.5 6-10a6 6 0 0 0-6-6zm0 8.5A2.5 2.5 0 1 1 6 3.5a2.5 2.5 0 0 1 0 5z" fill="#8cc63f"/></svg>WILLOW LAKES</h3>
    <p>Orchard Street, Willow Lakes Centre, 4068</p>
    <p><b>p:</b> 07 5550 4425<span class="mail"><b>e:</b> elmwood@purelyrooted.com.au</span></p>
  </div>
  <div class="location" style="top:465px">
    <h3><svg width="12" height="16" viewBox="0 0 12 16"><path d="M6 0a6 6 0 0 0-6 6c0 4.5 6 10 6 10s6-5.5 6-10a6 6 0 0 0-6-6zm0 8.5A2.5 2.5 0 1 1 6 3.5a2.5 2.5 0 0 1 0 5z" fill="#8cc63f"/></svg>RIVERSIDE GENERAL HOSPITAL</h3>
    <p>Larkin St, Eastvale, 4029</p>
    <p><b>p:</b> 07 5550 5519<span class="mail"><b>e:</b> rgh@purelyrooted.com.au</span></p>
  </div>

  <div class="web">WWW.PURELYROOTED.COM.AU</div>
</section>

<section class="card card-back">
  <div class="leaf-art" role="img" aria-label="Faint illustration of tropical leaves and fronds"></div>

  <div class="brand"><span class="brand-dot"></span>Purely Rooted Hair Salons</div>

  <div class="note">*Pricing is indicative of average products used and time taken for each service.<br>You will always receive a firm price after your consultation.<br>S to the jaw line | M to the collarbone | L to the bra strap | Xl past bra strap</div>

  <div class="menu menu-left">
    <div class="head" style="top:144px">CUT &amp; BLOW-DRY<span class="h1">S</span><span class="h2">M</span><span class="h3">L</span><span class="h4">XL</span></div>
    <div class="rule" style="top:175px"></div>
    <div class="row cap" style="top:185px">LADIES<span class="c1">$77</span><span class="c2">$88</span><span class="c3">$99</span><span class="c4">$110</span></div>
    <div class="row cap" style="top:199px">FRINGE</div>
    <div class="row" style="top:215px">Trim<span class="c1">$25</span></div>
    <div class="row" style="top:231px">Restyle<span class="c1">$35</span></div>
    <div class="row cap" style="top:245px">MENS</div>
    <div class="row" style="top:261px">Single blade clipper<span class="c1">$28</span></div>
    <div class="row" style="top:276px">Style cut<span class="c1">$42</span></div>
    <div class="row cap" style="top:291px">CHILDREN</div>
    <div class="row" style="top:307px">10 and under<span class="c1">$24</span></div>
    <div class="row" style="top:322px">11-16 Male<span class="c1">$32</span></div>
    <div class="row" style="top:338px">11-16 Female<span class="c1">$48</span></div>
    <div class="row" style="top:353px">add a wash<span class="c1">$5</span></div>
    <div class="row cap" style="top:368px">BLOWDRY<span class="c1">$47</span><span class="c2">$57</span><span class="c3">$67</span><span class="c4">$77</span></div>
    <div class="row" style="top:383px">Shampoo &amp; dry off<span class="c1">$25</span></div>

    <div class="head" style="top:413px">TREATMENTS</div>
    <div class="rule" style="top:445px"></div>
    <div class="row" style="top:455px">Deep treatment<span class="c1">$35</span></div>
    <div class="row" style="top:471px">Head.Spa ritual<span class="c1">$65</span></div>

    <div class="head" style="top:499px">UPSTILE</div>
    <div class="rule" style="top:531px"></div>
    <div class="row" style="top:541px">45 minutes<span class="c1">$85</span></div>
    <div class="row" style="top:558px">60 minutes<span class="c1">$120</span></div>
  </div>

  <div class="menu menu-right">
    <div class="head" style="top:144px">COLOUR<span class="h1">S</span><span class="h2">M</span><span class="h3">L</span><span class="h4">XL</span></div>
    <div class="rule" style="top:175px"></div>
    <div class="row cap" style="top:185px">REGROWTH<span class="c1">$83</span></div>
    <div class="row cap" style="top:200px">FULL COLOR TINT<span class="c1">$125</span><span class="c2">$145</span><span class="c3">$165</span><span class="c4">$185</span></div>
    <div class="row cap" style="top:215px">REGROWTH LIGHTENING<span class="c1">$165</span><span class="c2">$189</span><span class="c3">$209</span><span class="c4">$229</span></div>
    <div class="row cap" style="top:231px">BALAYAGE/OMBRE<span class="c2">$275</span><span class="c3">$375</span><span class="c4">$475</span></div>

    <div class="head" style="top:258px">VELIN GLOSS</div>
    <div class="rule" style="top:289px"></div>
    <div class="row cap" style="top:300px">REGROWTH<span class="c1">$99</span></div>
    <div class="row cap" style="top:315px">FULL COLOR TINT<span class="c1">$155</span><span class="c2">$175</span><span class="c3">$195</span><span class="c4">$205</span></div>

    <div class="head" style="top:344px">FOILS</div>
    <div class="rule" style="top:376px"></div>
    <div class="row cap" style="top:385px">SINGLE<span class="c1">$11</span><span class="c2">$13</span><span class="c3">$17</span><span class="c4">$22</span></div>
    <div class="row cap" style="top:401px">1/4 HEAD<span class="c1">$135</span><span class="c2">$155</span><span class="c3">$175</span><span class="c4">$195</span></div>
    <div class="row cap" style="top:416px">1/2 HEAD<span class="c1">$185</span><span class="c2">$205</span><span class="c3">$235</span><span class="c4">$265</span></div>
    <div class="row cap" style="top:432px">FULL HEAD<span class="c1">$235</span><span class="c2">$265</span><span class="c3">$315</span><span class="c4">$355</span></div>

    <div class="head" style="top:460px">STRAIGHT</div>
    <div class="rule" style="top:492px"></div>
    <div class="row cap" style="top:502px">KERATIN STRAIGHTENING SYSTEM<span class="c1">$365</span><span class="c2">$445</span><span class="c3">$535</span><span class="c4">$565</span></div>
    <div class="row" style="top:517px">Including colour mach &amp; toner</div>
    <div class="row" style="top:533px">Minimum 6 foils without colour</div>
    <div class="row" style="top:549px">Minimum change on a Sunday is $40</div>
  </div>
</section>

</body>
</html>
```